Pelverhook LLC
Business Cards & Stationary
Professional
Tobias Wendell
President
482 Orchard Crest Road
Dunmore Falls, NJ 07934-2718
tobias.wendell@mailvexo.com
www.pelverhook.com
I require the full suite of stationary products i.e.:- Business card, letterhead, envelope, fax cover sheet, thank you cards, invoice etc.
Just the logo on the back of the card.

```html
<!DOCTYPE html>
<html lang="en">
<head>
<meta charset="utf-8">
<title>Pelverhook LLC – Business Card</title>
<link rel="stylesheet" href="https://fonts.googleapis.com/css2?family=PT+Sans:wght@400;700&display=swap">
<style>
  :root {
    --page-bg: #ece8e2;
    --card-bg: #ffffff;
    --card-edge: #d9dde2;
    --band-blue: #2c63ad;
    --band-blue-dark: #1f4f93;
    --band-blue-light: #5b8ccd;
    --brand-blue: #1f5aa6;
    --text-dark: #2b2f36;
    --text-muted: #6c7480;
    --emblem-tone: #dfe6ee;
  }
  * { box-sizing: border-box; margin: 0; padding: 0; }
  html, body {
    width: 1200px; height: 780px; overflow: hidden;
    background: var(--page-bg);
    font-family: "PT Sans", Arial, sans-serif;
  }
  .card {
    position: absolute; left: 60px; top: 81px;
    width: 1080px; height: 618px;
    background: var(--card-bg);
    border-radius: 34px;
    border: 1px solid var(--card-edge);
    box-shadow: 0 8px 24px rgba(0,0,0,0.12);
    overflow: hidden;
  }
  .title-band {
    position: absolute; left: 0; top: 92px; width: 100%; height: 100px;
    background: linear-gradient(180deg, var(--band-blue-light) 0%, var(--band-blue) 45%, var(--band-blue-dark) 100%);
    border-top: 3px solid #ffffff;
    box-shadow: 0 -2px 0 var(--band-blue-dark);
  }
  .holder {
    position: absolute; right: 62px; top: 110px; text-align: right; color: #ffffff;
  }
  .holder-name { font-size: 36px; font-weight: 700; line-height: 1.1; }
  .holder-role { font-size: 21px; font-weight: 400; line-height: 1.2; opacity: 0.95; }
  .emblem-fade {
    position: absolute; left: 700px; top: 150px; width: 330px; height: 330px;
    border-radius: 50%;
    background: radial-gradient(circle at 55% 45%, var(--emblem-tone) 0%, #eef2f6 55%, rgba(255,255,255,0) 72%);
  }
  .brand {
    position: absolute; left: 110px; top: 120px; width: 440px; text-align: center;
  }
  .brand-mark {
    display: block; margin: 0 auto 14px;
    width: 150px; height: 150px; border-radius: 50%;
    background: #ffffff; border: 6px solid var(--brand-blue);
  }
  .brand-name {
    font-size: 58px; font-weight: 700; color: var(--brand-blue);
    letter-spacing: 1px; line-height: 1;
  }
  .brand-tagline {
    margin-top: 8px; font-size: 14px; letter-spacing: 3px; color: var(--brand-blue);
    text-transform: uppercase;
  }
  .address {
    position: absolute; left: 108px; top: 452px;
    font-size: 23px; line-height: 1.3; color: var(--text-dark);
  }
  .contacts {
    position: absolute; left: 108px; top: 528px;
    display: grid; grid-template-columns: 190px auto; row-gap: 14px; column-gap: 10px;
    font-size: 23px; color: var(--text-dark);
  }
  .contact { display: flex; align-items: center; gap: 10px; white-space: nowrap; }
  .contact svg { width: 24px; height: 24px; fill: var(--brand-blue); flex: none; }
</style>
</head>
<body>
  <div class="card">
    <div class="title-band"></div>
    <div class="emblem-fade" role="img" aria-label="Faint mountain and pine tree emblem"></div>

    <div class="holder">
      <div class="holder-name">Tobias Wendell</div>
      <div class="holder-role">President</div>
    </div>

    <div class="brand">
      <span class="brand-mark"></span>
      <div class="brand-name">PELVERHOOK</div>
      <div class="brand-tagline">Consulting · Investments · Advisors</div>
    </div>

    <div class="address">
      482 Orchard Crest Road<br>
      Dunmore Falls, NJ 07934-2718
    </div>

    <div class="contacts">
      <div class="contact">
        <svg viewBox="0 0 24 24" aria-hidden="true"><path d="M6.6 10.8c1.4 2.8 3.8 5.1 6.6 6.6l2.2-2.2c.3-.3.7-.4 1-.2 1.1.4 2.3.6 3.6.6.6 0 1 .4 1 1V20c0 .6-.4 1-1 1C10.6 21 3 13.4 3 4c0-.6.4-1 1-1h3.5c.6 0 1 .4 1 1 0 1.3.2 2.5.6 3.6.1.3 0 .7-.2 1z"/></svg>
        555.318.4402
      </div>
      <div class="contact">
        <svg viewBox="0 0 24 24" aria-hidden="true"><path d="M7 2h10a2 2 0 0 1 2 2v16a2 2 0 0 1-2 2H7a2 2 0 0 1-2-2V4a2 2 0 0 1 2-2zm0 3v12h10V5zm5 13.5a1.2 1.2 0 1 0 0 2.4 1.2 1.2 0 0 0 0-2.4z"/></svg>
        555.318.4417
      </div>
      <div class="contact">
        <svg viewBox="0 0 24 24" aria-hidden="true"><path d="M6 2h9l3 3v5h1a3 3 0 0 1 3 3v7a2 2 0 0 1-2 2H4a2 2 0 0 1-2-2v-7a3 3 0 0 1 3-3h1zm2 2v6h8V6h-2V4zm-2 10v2h3v-2zm5 0v2h3v-2zm5 0v2h3v-2zm-10 3v2h3v-2zm5 0v2h3v-2zm5 0v2h3v-2z"/></svg>
        555.318.4402
      </div>
      <div class="contact">
        <svg viewBox="0 0 24 24" aria-hidden="true"><path d="M3 5h18a1 1 0 0 1 1 1v12a1 1 0 0 1-1 1H3a1 1 0 0 1-1-1V6a1 1 0 0 1 1-1zm1 2.2V17h16V7.2l-8 5.3z M5 7l7 4.6L19 7z"/></svg>
        tobias.wendell@mailvexo.com
      </div>
    </div>
  </div>
</body>
</html>
```